New website for Scuba Diving School ‘FinTide’ in Dublin, Ireland

New website for Scuba Diving School ‘FinTide’ based in Dublin, Ireland.

GENERAL DESCRIPTION OF WHAT I WANT THIS WEBSITE TO BE:

Website must be professional and modern looking. It has to be user friendly so that everybody can easily find information they are looking for. I would like to see the site being innovative and funky yet still appeal to the main market which is 25-35 years old with 2/3 being male middle to high income.

Site should be creative with bright colours. As the site is for scuba diving school it should be cheerful and welcoming. Colours should be eye catching and worm to create friendly image from a very first time it’s visited. Images used in the website should stay as realistic as possible yet professional.

Home Page:
Section 1) Left up to you if you want anything above the menu bar.

Section 2) Under need I want to have menu bar that will have 6 main pages and 6 subpages. How you designed the menu bar is up to you as long as you stick the correct content:

Main Page 1. Home
Main Page 2. About Us
Main Page 3. Courses & Prices
Sub Page - Try a Dive Evening
Sub Page - Scuba Review
Sub Page - Beginners Course
Sub Page - Advanced Open water
Sub Page - Rescue Diver
Sub Page - DiveMaster Course
Main Page 4. Contact Us
Main Page 5. FAQ
Main Page 6. Calendar

Section 3)
I would like to stick to minimum text content on the main page but I would like to see the following:

Under the menu bar please create an image slide show that will change every couple of seconds or can be operated by user when clicked on dot, number or arrow. Example can be found on the fallowing website: http://www.velmorastream.example/?tv or http://www.quorvadive.example/scuba/ this is just to give you an idea. I want this slide show to be creative and promote all courses one by one. Pictures in the slide show must be relevant and professional. On each slide please use exact content provided below:

- 1st slide. Content: "Try a Dive Evening for ONLY 49€'
- 2nd slide Content: “Sign up Today for your Beginners Course"
- 3rd slide Content: "Kelvo Advanced Diver Course"
- 4th slide Content: "The Kelvo Rescue Diver Course"
- 5th slide Content: "LumaCam with Kelvo DiveMaster course"

Please link those slides with appropriate course pages so the user can be redirected directly to the course page.

Section 4)
On the bottom of the page I would like to see all links in columns in small print with my logo in the right bottom corner. Please make the logo clearly visible

ADDITIONAL INFORMATION:

Also, somewhere on the page I would like to see some form of a price tag that will attract user attention. The purpose of this price tag is for the user to click on it to check our discounts.

Content for the Price Tag: “MATES RATES 10%OFF” and when clicked it will bring up a pop up window that will state the following:
POP UP Content:

“Sign up now for our next "Try a Dive Evening" and get 10% when you come with your friend! Bring two friends and get 10% off of your next Beginners course"!
Contact us now to book your place!

‘Contact us’ should be a link that will redirect user to the ‘Contact Us’ Page. (This should be done on all pages) plus the link to the calendar page.

About us Page:

Section 1 and Section 2 from the home page should be repeated.

Section 3) Content:

This section will be information to give a customer overview of who we are and what we do. I will provide you with the picture in the next 3-4 day (waiting for the photographer to get back to me) which I would like to be included on this page with fallowing information: Tomas Lindqvy Kelvo No. 574830.
Also I would like this picture to be part of the fallowing content:
Please stick to exact wording:

Content:
Welcome to FinTide

We are Dublin based scuba diving school dedicated to teaching Scuba Diving in the internationally recognised KELVO diving system. We have a real passion for diving and love everything about the real magic that the underwater world has to offer.

We teach a range of courses starting from a very beginning right through to professional level diving. All our staffs are official Scuba Diving KELVO, RMT instructors and KELVO DiveMasters.

We take great pride in our professional approach to diving and can guarantee that that you will receive the highest level of expertise and attention available whether you are trying just one evening of scuba or completing your Dive Master program.

FinTide is a progressive Eco minded business promoting safe and responsible diving. In everything we do. Everybody who learns to scuba dive with us is taught that safety is at the heart of everything we do in Scuba. The whole worlds of the oceans are opened up to be discovered. We believe that we can all make a huge difference in keeping our oceans healthy and self-sustaining for the generations to come.

Meet our owner and KELVO qualified Instructor at FinTide.

“I am originally from Poland but moved to Ireland in 2006 and yes I have a Dublin accent now! When I started my adventures in diving here was keen to explore the wonders of many of great diving sites in Irelands surrounding coastline. I am a professionally qualified Kelvo Open Water Instructor and I really enjoy working with students on all levels. I have a genuine love and passion for the Irish waters and from the beginning when I sold my car to purchase my first diving equipment I knew this is the path in life that I want to take. I LOVE THE WATER! Most people probably don’t know that Ireland is one of the best places in the world for scuba diving. The diversity of marine life on Ireland’s coasts is absolutely fantastic. Now that we have a great Harbourview Swim Arena we have unrivalled facilities for people to start with scuba in the controlled surroundings before moving on to discover the great underwater world in the seas. I encourage everybody to give it a go and discover for themselves what turned my world upside down”.

Section 4)

Courses Page

Section 1 and Section 2 from the home page should be repeated on each course page. I don’t want all courses on one page that’s why I listed them as subpages in form of a dropdown menu. I want the customer to have a choice where they go so they can skip the information that is not relevant to them.

Please stick to the exact content provided below. Please use some images on each of the course pages to reflect the information provided for the customer. Again please make the images smaller so they add to the page and not still attention from the text.

Furthermore, please call each page in the drop down menu as you can see them in Section 2 of the home page.

• Subpage 1 ‘Try a Dive’
Content:
Discover Scuba Diving (Price Tag: Only 49€)
Have you ever seen those underwater documentaries and wish you could discover the amazing world of scuba for yourself? Or have you ever watched a scuba diver on TV and wondered if you could ever experience the fascinating world that exists under the sea? Or did you know Ireland has some of the most fascinating and diverse marine ecosystems in the world and they are right on our door step? Well now you can easily discover scuba for yourself in the comfort of the world class facilities at Dublin’s Harbourview Swim Arena under the direction and supervision of a FinTide Scuba Instructor.

This Discover Scuba Diving Kelvo program is a great introduction to the magical world of scuba. In the comfort of the swimming pool under watchful eye of your instructor you will get a chance to learn a few basics about scuba diving, practice some fun skills and familiarise yourself with scuba equipment

There is no need for previous experience or the ability to swim like an Olympian. You just need a towel and a swimsuit and we provide you with the rest.
Our Discover Scuba Diving night happens on Tuesday evenings 7-10pm using the facilities at the Harbourview Swim Arena.

It really is that simple so don’t wait any longer!

Contact us today to book your adventure now.

• Subpage 2 ‘Scuba Review’
Content:
Scuba Review (Price Tag: Only 59€)
If it been a while since you had a chance to dive with your buddy and your skills are a bit rusty or maybe you thinking of doing some scuba again on holiday then why not take part in this scuba review program to refresh your skills at the Harbourview Swim Arena

Kelvo Scuba Review was designed for anybody who is certified but has stopped diving for a while and would like to get back into the sport again .During this one- evening session our instructor will review your diving knowledge and help you practice your skills before you head back to the open water.

There is no requirement to take the full theory test again.

Simply contact us to complete your Scuba Review!

• Subpage 3 ‘Beginners Course’
Content:
Open Water Diver (Price Tag: Only 559€)
The KELVO Open Water course opens the door of a whole new world of discovery. Everything that happens underwater from discovering our amazing diverse marine life to diving to see long lost ship wrecks all begins with completing your first Open Water course. Once you have completed this course you will be awarded your own internationally recognized scuba diving license which allows you to explore the wonderful world of scuba on any future holidays or international travels.

If you've always wanted to learn how to scuba dive, this course is the best way to start. The KELVO Open Water Diver course is the world's most popular scuba course, and has introduced millions of people to the adventurous diving lifestyle.

Breathing under water for the first time is something new and unforgettable. Our Kelvo Open Water course is structured in a way that allows you to study at your own comfortable pace. The course teaches you the scuba diving theory behind diving, and allows you to practice your diving skills in the comfort of the swimming pool in the world class facility of the Harbourview Swim Arena. We will then take you out into the sea for your open water dives to allow you practice your new scuba diving skills under our professional supervision.

We designed our courses to fit your busy life style. Our classroom and pool training takes place every Tuesday in Harbourview Swim Arena from 7 to 10 pm. Once you have enough knowledge of the scuba diving basics completed in the pool we will then take you diving in the open water at one of the great local dive sites. We offer a high degree of flexibility to people completing the course and if you do miss some classes we schedule extra time at no extra cost to allow your course completion.

Our course runs over a period of six weeks. Five evening’s sessions in the pool and one weekend at one of our regular dive sites.

What you need is a towel and a swimsuit the rest will be provided.
You can start your Open Water Diver course today by simply getting in touch with us by clicking on Contact us.

• Subpage 4 ‘Advanced Open water’
Content:
Advanced Open Water Diver (Price Tag: Only 389€)

Keeping your diving skills sharp is an important part of scuba diving. Once you have completed your Open Water scuba course and begin to feel comfortable with your dives then you may decide you wish to learn additional diving skills, undertake some deeper dives and further develop your knowledge of scuba diving. Our Advance Open Water Course is specially designed for this purpose.

This course is structured in a way that enables you to learn more about the various different types of diving. It includes 5 great adventure dives that will allow you maximize the enjoyment of your diving skills and as safety is always our priority the course is completed under the guidance of our experienced qualified FinTide instructor.
This course involves some theory without the need for final exam so you will have more time to enjoy some of our awesome dive sites.

This course is only suitable if you have already completed your KELVO Open Water Diver (or qualifying certification from another training organization). But remember You don't need to have your own diving equipment as FinTide will provide everything you need for course participation.

The course is conducted over one weekend and we run advanced courses regularly all year round. If you can't make it on the weekends we can also run it during the week.
You can start your Advanced Open Water Diver course today by simply getting in touch with us by clicking on Contact us.

• Subpage 5 ‘Rescue Diver’
Content:
Rescue Diver (Price Tag: Only 369€)

Scuba diving is one of the most enjoyable and fulfilling activities experienced by thousands of people around the world every day. The popularity of recreational diving continues to increase every year. The diving community places safety as our number one primary concern for all participants in the sport.

The Kelvo Recue Diver program is designed to teach you the skills and give you the appropriate training which can help prevent emergency situations to occur. You will also receive training on the best practices required to help manage an emergency situation. Certified Kelvo Rescue Divers look back on their rescue training as one of the most challenging – sometimes demanding- and therefore one of the most rewarding programs they’ve taken.

If you dive very often then eventually you may find yourself in a situation where you, your buddy or a fellow diver may need some help or assistance. This course teaches you the skills and knowledge required to take control of a rescue situation.

If you are thinking of working towards further professional ratings such as DiveMaster then this is a valuable step along the way.

To participate in this course you must have a current first aid & CPR certificate and have completed a KELVO Advanced Open Water Diver (or a similar qualifying rating) prior to starting the Rescue course.

The course is combined with class room and pool training in the Harbourview Swim Arena and open water training is completed at one of our dive sites.

If you are interested in our Kelvo Rescue diver program then Contact us here...

• Subpage 6 ‘DiveMaster Course’
Content:
DiveMaster Program (Price Tag: Only 559€)

If you are really serious about your scuba diving then you should consider qualifying as a KELVO DiveMaster with FinTide. The KELVO DiveMaster course is the first level of the KELVO Professional ratings. As a KELVO DiveMaster you will hold the minimum rating for employment in the diving industry. Your qualification will allow you to supervise recreational diving activities (either boat or land based), work as an Instructional assistant on all KELVO courses and is just one step away from a KELVO Instructor rating.

Working closely with a KELVO Instructor, in this program you expand your dive knowledge and hone your skills to the professional level. KELVO DiveMaster training develops your leadership abilities, qualifying you to supervise dive activities and assist instructors with student divers. KELVO DiveMaster is the prerequisite certification for both the KELVO Assistant Instructor and KELVO Open Water Scuba Instructor certifications.

After successfully completing your DiveMaster course you will earn the title of DiveMaster and be authorized to:
• Supervise both training and non-training-related activities by planning, organizing and directing dives
• Assist a KELVO Instructor during the training sessions for any KELVO Diver course
• Conduct the KELVO Skin Diver course and KELVO Discover Snorkelling program
• Conduct the KELVO Discover Local Diving experience
• Conduct the KELVO Scuba Review program
• If qualified as a Discover Scuba Diving Leader, independently conduct the KELVO Discover Scuba Diving program.
• Earn the KELVO Digital Underwater Photographer Specialty Instructor rating to be able to teach the KELVO Digital Underwater Photographer specialty.
• Independently guide Open Water Diver course students on the tour portion of Open Water Diver course Training Dives 2, 3 and 4 at a ratio of two student divers per certified DiveMaster.
• Accompany Open Water Diver students under the indirect supervision of a KELVO Instructor during:
o surface swims to and from the entry/exit point and during navigational exercises
o when the instructor conducts a skill, such as an ascent or descent, a DiveMaster can remain with other student divers (with an individual student or buddy team)
• Accompany student divers during Adventure Dives or Specialty training dives under the indirect supervision of a KELVO Instructor.
• Conduct the KELVO Otter Squad Skin Diver Specialist WaveQuest
• Conduct subsequent dives under an instructor’s indirect supervision for Discover Scuba Diving participants after participants have satisfactorily completed the first dive with a KELVO Instructor.
• Teach Rapid Medical Training courses after successfully completing an Rapid Medical Training Instructor course.

You also gain access to exclusive Kelvo Pro site with many benefits such as Job forums for dive professionals.

To complete this course there are some minimum requirements you must be:

• 18 years old and KELVO Advanced Open Water Diver (or qualifying certification from another training organization
• A KELVO Rescue Diver (or qualifying certification from another training organization)
• An Rapid Medical Training Primary and Secondary Care (or qualifying first aid and CPR training from another organization) course completion within the past 24 months.
• Have at least 40 dives to begin the course and 60 for certification
• Be fit for diving and submit a Medical Statement signed by a physician within the last 12 months.
• Have your own equipment
What can you expect completing your KELVO DiveMaster with FinTide?
FinTide manage the qualification process as a DiveMaster with a very high degree of personal teaching. We are not a high volume ‘factory style ‘diving school. We offer a personal friendly environment encouraging you to develop your diving skills in an enjoyable way. Typically we will only enrol a maximum of 3 interns at one time. We ensure to offer very thorough training and our goal is to make you an employable, experienced member of the worldwide professional diving community.

You will be “immersed” in the world of scuba diving. In addition to your learning you also will be working alongside your instructor during all recreational level courses so you can learn how a run courses, coordinate dive trips, supervise divers in the water and learning your own teaching skills.

To be awarded as Kelvo DiveMaster you will need to complete and pass fallowing:
• Complete knowledge development sessions and pass the DiveMaster final exam
• Create an Emergency Assistance plan
• Complete waters kills exercises
• Complete a diver rescue assessment
• Complete the dive skill workshop and assessment
• Complete practical application skills
• Complete DiveMaster-conduct programs workshop
• Complete practical assessment
As you can see the KELVO DiveMaster program with FinTide is a very comprehensive diving program suitable for anyone who is enthusiastic or serious about Scuba Diving. The program usually takes between 3 and 6 months to complete. If you interested in finding out more about qualifying as a Kelvo DiveMaster with FinTide then simply contact us and we will discuss the process and answer any questions you may have.

What are the total costs involved in the DiveMaster Program?

The KELVO DiveMaster Program with FinTide costs 559€.Fees can be payable in instalments over the course of the program. Your KELVO DiveMaster crew pack will cost 180€.
If you are interested in completing your Kelvo DiveMaster program contact us and a FinTide Diving Instructor will be happy to answer any questions you may have.

Section 4)

Contact us Page:

Section 3)
This section is the ‘contact’ form. The actual image of the contact for is left up to you but please create the form so I can receive the fallowing information:

Name
E-mail address
Contact Number
Text (2000 symbol minimum so user can send us email without the need of contacting us twice)

Under need please add Mapora map that will allow users to locate the Harbourview Swim Arena in Dublin, Ireland.

Section 4)

FAQ Page

Section 3) those are actual questions and answer that I would like to see:

Q Who can do scuba diving?
A: Anyone in good health can do scuba diving.

Q Do I have to pay all my fees upfront for courses?
A. For open water diver and above we only require a 20% deposit on the first night and the rest can be paid over the period of your course

Q I don’t have any scuba equipment is this a problem?
A: No, all your equipment will be provided for you by us

Q Do I need to consider insurance to go scuba diving with FinTide?
A: No, all our students are covered by our insurance

Q. Where do I purchase books for the scuba courses you offer?
A All your Kelvo Studding Materials will be supplied by us

Q If I am unable to dive due to illness do I miss out on my course?
A No, if you miss a course dive we simply schedule extra time at no extra cost

Q Is the Irish weather a major problem ?
A The great thing about discovering Scuba with us is that all our intimal training is at the indoor facilities at the Harbourview Swim Arena. For your safety and comfort we always reschedule open water dives for suitable weather conditions

Q Can I take exams in my native language?
A Yes study material are available in all languages, just inform us before you start your course.

Q Can I go diving without the appropriate training?
A No, for safety you are required to complete training course before diving.

Section 4)

Calendar Page:

Section 3)
I would like to have active calendar which I can update myself so that users can see upcoming courses:

Please make sure that calendar is active and that current date in highlighted. I don’t want the user to be under the impression that our calendar is simple copy past picture.
Due to unpredictable weather patterns in Ireland I need to be able to update calendar myself.

Section 4)

Addition Information: In the next couple of months (2-4) I would like to add few subpages to this website to promote more diving courses. So there will be a chance of extra income for the person who will design this site.

If you need any more information feel free to contact me.

Kind Regards and Thanks to all of you for taking on this project.
Tomas Lindqvy
Updates

Hello,

First of all I would like to say massive thanks for all work so far and I would like to apologize for not attaching my logo to my brief. I just corrected this so you have access to it.

Thanks,
Tomas Lindqvy

Target Market(s)

basics statistics can be found: http://www.quorvadive.example/scuba/about-quorva/quorva-statistics/Default.aspx

Industry/Entity Type

Progressive

Requirements
Must have
• Active calendar so i can update courses myself
Nice to have
• maybe date and clock in the corner just for esthetic apperance
Should not have
• complicated layout or menu bar that is not practical and clearly visible

```html
<!DOCTYPE html>
<html lang="en">
<head>
<meta charset="utf-8">
<title>FinTide – Scuba Diving School Dublin</title>
<link rel="stylesheet" href="https://fonts.googleapis.com/css2?family=Noto+Serif:wght@700&family=Arimo:wght@400;700&display=swap">
<style>
:root{
  --sky-top:#6fb2e4;
  --sky-low:#d6ecf8;
  --sea-top:#0fa3ee;
  --sea-mid:#0a8fe6;
  --sea-deep:#0b6fc4;
  --reef-a:#2d6f8c;
  --reef-b:#5d6a62;
  --nav:#4a6f98;
  --accent-red:#c0272d;
  --menu-red:#b02426;
  --menu-line:#c8454a;
  --frame:#3fe6f4;
  --white:#ffffff;
  --yellow:#f5e92a;
  --panel:#0b5ea8;
  --panel-line:#3b86c6;
  --cal-bg:#e9eaeb;
  --cal-cell:#f7f7f7;
  --cal-text:#444;
  --today:#4cc3ee;
  --btn-top:#6fd2fb;
  --btn-low:#1ca6ea;
  --footer:rgba(10,30,45,.55);
}
*{box-sizing:border-box;margin:0;padding:0}
html,body{width:1200px;height:1110px;overflow:hidden}
body{position:relative;font-family:"Arimo",Arial,sans-serif;color:var(--white);
  background:linear-gradient(180deg,var(--sky-top) 0,var(--sky-low) 120px,#9fd3f2 140px,var(--sea-top) 158px,var(--sea-mid) 520px,#0d8fe8 760px,var(--sea-deep) 900px,var(--reef-a) 980px,var(--reef-b) 1110px)}
.abs{position:absolute}
a{color:inherit;text-decoration:none}

.reef{left:0;top:760px;width:1200px;height:350px;background:linear-gradient(180deg,rgba(60,120,140,0) 0,rgba(70,110,120,.55) 45%,rgba(95,95,85,.75) 100%)}
.diver-photo{left:1014px;top:321px;width:186px;height:490px;background:linear-gradient(180deg,rgba(12,110,200,0) 0,rgba(10,80,160,.35) 40%,rgba(10,80,160,.35) 70%,rgba(12,110,200,0) 100%)}

.brand{left:193px;top:52px;display:flex;align-items:center;gap:8px;font-family:"Noto Serif",Georgia,serif;font-weight:700;font-size:34px;color:var(--accent-red)}
.brand .dot{width:22px;height:22px;border-radius:50%;background:var(--accent-red)}

.search{left:812px;top:18px;width:205px;height:28px;border-radius:6px;background:linear-gradient(#f2f5f8,#c9d6e2);border:1px solid #9fb7cc;font-size:10.5px;color:#5b6770;padding:8px 10px}
.search svg{position:absolute;right:11px;top:7px}

.nav{left:480px;top:82px;display:flex;list-style:none;font-family:"Noto Serif",Georgia,serif;font-weight:700;font-size:14px;color:var(--nav)}
.nav li{padding:0 10px;border-left:1px solid #8eaec9;line-height:18px}
.nav li:first-child{border-left:0;padding-left:0}
.nav li:last-child{padding-right:0}
.nav .active{color:var(--accent-red)}

.dropdown{left:635px;top:113px;width:184px;height:172px;background:var(--menu-red);border-radius:6px;padding:6px 9px;list-style:none;font-family:"Noto Serif",Georgia,serif;font-weight:700;font-size:11.5px}
.dropdown::before{content:"";position:absolute;left:32px;top:-8px;border:8px solid transparent;border-top:0;border-bottom-color:var(--menu-red)}
.dropdown li{height:25.4px;line-height:25px;border-bottom:1px solid var(--menu-line);padding-left:14px;position:relative;white-space:nowrap}
.dropdown li:last-child{border-bottom:0}
.dropdown li::before{content:"›";position:absolute;left:3px;top:0;font-size:11px}

.slider{left:190px;top:167px;width:820px;height:364px;border:4px solid var(--frame);border-radius:6px;background:linear-gradient(160deg,#1f5f8f 0,#2b7fa8 40%,#2f9bb2 70%,#3aa9b0 100%)}
.slide-text{left:226px;top:436px;font-family:"Noto Serif",Georgia,serif;font-weight:700;font-size:23.5px;line-height:43px;text-shadow:0 1px 3px rgba(0,0,0,.5)}
.slide-text .hl{color:var(--yellow)}
.arrow{top:330px;width:41px;height:38px;border-radius:4px;background:linear-gradient(#ffffff,#cfe6f6);box-shadow:0 1px 3px rgba(0,0,0,.3);display:flex;align-items:center;justify-content:center}
.arrow.prev{left:177px}.arrow.next{left:982px}

.welcome h1{position:absolute;left:193px;top:556px;font-family:"Noto Serif",Georgia,serif;font-weight:700;font-size:19.5px;white-space:nowrap}
.welcome p{position:absolute;left:193px;width:500px;font-size:10.2px;line-height:18.6px;color:#eaf6ff;text-align:justify}
.p1{top:597px}.p2{top:672px}
.btn{left:189px;top:729px;width:103px;height:38px;border-radius:8px;background:linear-gradient(var(--btn-top),var(--btn-low));border:1px solid #a9e6ff;font-size:13px;line-height:36px;text-align:center}

.video{left:711px;top:560px;width:293px;height:199px;border-radius:10px;border:3px solid #0e6fc0;background:linear-gradient(170deg,#1b66c8,#0f3d9a 60%,#0a2f7a)}
.play{left:836px;top:640px}

.divider{left:190px;top:790px;width:820px;height:1px;background:rgba(255,255,255,.3)}

.calendar{left:189px;top:811px;width:193px;height:184px;background:var(--cal-bg);border-radius:4px 0 0 4px;color:var(--cal-text)}
.cal-head{height:25px;border-bottom:1px solid #cfd1d3;font-size:9.5px;line-height:25px;text-align:center;position:relative}
.cal-head span{position:absolute;top:0;font-size:7px;color:#777}
.cal-grid{display:grid;grid-template-columns:repeat(7,21px);gap:4.5px 4.4px;padding:6px 9px 0 9px}
.cal-grid .dow{font-size:7.5px;text-align:center;color:#666}
.cal-grid .d{height:21px;background:var(--cal-cell);border:1px solid #d3d5d7;border-radius:3px;font-size:9px;font-weight:700;text-align:center;line-height:19px}
.cal-grid .muted{color:#c4c4c4}
.cal-grid .today{background:var(--today);border-color:#37a8d6;color:#1c5f85}

.events{left:382px;top:811px;width:628px;height:184px;background:var(--panel);border-radius:0 4px 4px 0;border:1px solid #2b7dc4}
.events h2{position:absolute;left:13px;top:12px;font-family:"Noto Serif",Georgia,serif;font-weight:700;font-size:14px}
.events .rule{position:absolute;left:10px;right:10px;top:37px;height:1px;background:var(--panel-line)}
.ev-nav{position:absolute;right:15px;top:12px;display:flex;gap:1px}
.ev-nav i{width:14px;height:16px;background:#2c8ad6;display:flex;align-items:center;justify-content:center}
.ev-nav i:first-child{border-radius:8px 0 0 8px}.ev-nav i:last-child{border-radius:0 8px 8px 0}
.ev-photo{position:absolute;left:14px;top:58px;width:118px;height:110px;border-radius:8px;border:2px solid #5aa9e4;background:linear-gradient(160deg,#6aa7d8,#2f4f86 60%,#1a2c55)}
.ev-title{position:absolute;left:140px;top:60px;font-size:12.5px;color:var(--yellow);white-space:nowrap}
.ev-body{position:absolute;left:140px;top:89px;width:440px;font-size:10px;line-height:18.6px;color:#e6f2fc}
.ev-body a{color:var(--yellow)}
.ev-meta{position:absolute;left:450px;top:155px;display:flex;align-items:center;font-size:10px;font-weight:700;gap:6px}

.footer{left:0;top:1032px;width:1200px;height:78px;background:linear-gradient(rgba(10,30,45,0),var(--footer) 20px)}
.foot-links{left:197px;top:1044px;font-size:10.5px;display:flex;gap:0}
.foot-links a{padding:0 5px;border-left:1px solid rgba(255,255,255,.6);line-height:11px}
.foot-links a:first-child{border-left:0;padding-left:0}
.copy{left:197px;top:1068px;font-size:10.5px}
.social{left:838px;top:1050px;display:flex;gap:11px;list-style:none}
.social li{width:26px;height:26px;border-radius:50%;background:linear-gradient(#f1f6fa,#b9ccda);border:1px solid rgba(255,255,255,.6)}
</style>
</head>
<body>

<div class="abs reef" role="img" aria-label="Coral reef seabed along the bottom of the page"></div>
<div class="abs diver-photo" role="img" aria-label="Photo of a scuba diver with a camera rising among bubbles"></div>

<a class="abs brand" href="#"><span class="dot"></span>FinTide</a>

<div class="abs search">Search
  <svg width="12" height="12" viewBox="0 0 12 12"><circle cx="5" cy="5" r="3.4" fill="none" stroke="#c0272d" stroke-width="1.8"/><line x1="7.5" y1="7.5" x2="11" y2="11" stroke="#c0272d" stroke-width="2"/></svg>
</div>

<ul class="abs nav">
  <li><a href="#">HOME</a></li>
  <li><a href="#">ABOUT US</a></li>
  <li class="active"><a href="#">COURSES &amp; PRICES</a></li>
  <li><a href="#">CONTACT US</a></li>
  <li><a href="#">FAQ</a></li>
  <li><a href="#">CALENDAR</a></li>
</ul>

<div class="abs slider" role="img" aria-label="Photo of four smiling divers in masks swimming toward the camera over a reef"></div>
<div class="abs slide-text">
  <div>Try a Dive Evening for ONLY <span class="hl">49€</span></div>
  <div><span class="hl">Sign up Today</span> for your Beginners Course</div>
</div>
<a class="abs arrow prev" href="#"><svg width="12" height="18" viewBox="0 0 12 18"><path d="M10 2 3 9l7 7" fill="none" stroke="#2f7fc0" stroke-width="3"/></svg></a>
<a class="abs arrow next" href="#"><svg width="12" height="18" viewBox="0 0 12 18"><path d="M2 2l7 7-7 7" fill="none" stroke="#2f7fc0" stroke-width="3"/></svg></a>

<ul class="abs dropdown">
  <li>TRY A DIVE EVENING</li>
  <li>SCUBA REVIEW</li>
  <li>BEGINNERS COURSE</li>
  <li>ADVANCED OPEN WATER</li>
  <li>RESCUE DIVER</li>
  <li>DIVEMASTER COURSE</li>
</ul>

<section class="welcome">
  <h1>WELCOME TO OUR FINTIDE</h1>
  <p class="p1">We are Dublin based scuba diving school dedicated to teaching Scuba Diving in the internationally recognised KELVO diving system. We have a real passion for diving and love everything about the real magic that the underwater world has to offer.</p>
  <p class="p2">We teach a range of courses starting from a very beginning right through to professional level diving. All our staffs are official Scuba Diving KELVO, RMT instructors and KELVO DiveMasters.</p>
</section>
<a class="abs btn" href="#">READ MORE</a>

<div class="abs video" role="img" aria-label="Video still of two divers swimming in deep blue water"></div>
<svg class="abs play" width="42" height="42" viewBox="0 0 42 42"><circle cx="21" cy="21" r="19" fill="#eef5fb" stroke="#9cc3e3" stroke-width="2"/><path d="M16 12l13 9-13 9z" fill="#2a6fb8"/></svg>

<div class="abs divider"></div>

<div class="abs calendar">
  <div class="cal-head"><span style="left:9px">◀</span>FEBRUARY<span style="right:9px">▶</span></div>
  <div class="cal-grid">
    <div class="dow">MON</div><div class="dow">TUE</div><div class="dow">WED</div><div class="dow">THU</div><div class="dow">FRI</div><div class="dow">SAT</div><div class="dow">SUN</div>
    <div class="d">1</div><div class="d">2</div><div class="d">3</div><div class="d">4</div><div class="d">5</div><div class="d">6</div><div class="d">7</div>
    <div class="d">8</div><div class="d">9</div><div class="d">10</div><div class="d">11</div><div class="d">12</div><div class="d">13</div><div class="d">14</div>
    <div class="d">15</div><div class="d">16</div><div class="d">17</div><div class="d today">18</div><div class="d">19</div><div class="d">20</div><div class="d">21</div>
    <div class="d">22</div><div class="d">23</div><div class="d">24</div><div class="d">25</div><div class="d">26</div><div class="d">27</div><div class="d">28</div>
    <div class="d">29</div><div class="d">30</div><div class="d">31</div><div class="d muted">1</div><div class="d muted">2</div><div class="d muted">3</div><div class="d muted">4</div>
  </div>
</div>

<section class="abs events">
  <h2>FEATURED EVENTS</h2>
  <div class="ev-nav">
    <i><svg width="6" height="8" viewBox="0 0 6 8"><path d="M5 1 2 4l3 3" fill="none" stroke="#fff" stroke-width="1.5"/></svg></i>
    <i><svg width="6" height="8" viewBox="0 0 6 8"><path d="M1 1l3 3-3 3" fill="none" stroke="#fff" stroke-width="1.5"/></svg></i>
  </div>
  <div class="rule"></div>
  <div class="ev-photo" role="img" aria-label="Photo of a young diver wearing a mask and snorkel"></div>
  <div class="ev-title">Praesent vestibulum molestie lacus. Aenean nonummy hendrerit mauris</div>
  <p class="ev-body">Fusce suscipit varius mi. Cum sociis natoque penatibus et magnis dis parturient montes, nascetur ridiculus mus. Nulla dui. Fusce feugiat malesuada odio. Morbi nunc odio, gravida at, cursus nec, luctus a, lorem. Maecenas tristique orci ac sem. &nbsp;<a href="#">Read more.....</a></p>
  <div class="ev-meta">
    <svg width="18" height="17" viewBox="0 0 18 17"><rect x="1" y="3" width="16" height="13" rx="1" fill="#fff"/><rect x="1" y="3" width="16" height="4" fill="#3a9be0"/><rect x="4" y="0.5" width="2" height="4" fill="#1d6fb3"/><rect x="12" y="0.5" width="2" height="4" fill="#1d6fb3"/><g fill="#3a9be0"><rect x="3" y="9" width="2" height="2"/><rect x="7" y="9" width="2" height="2"/><rect x="11" y="9" width="2" height="2"/><rect x="3" y="12" width="2" height="2"/><rect x="7" y="12" width="2" height="2"/></g></svg>
    <span>FEB 18, 2013</span>
    <svg style="margin-left:8px" width="18" height="18" viewBox="0 0 18 18"><circle cx="9" cy="9" r="8" fill="#fff" stroke="#8cc6ef" stroke-width="1.5"/><path d="M9 4v5l3 2" fill="none" stroke="#3a9be0" stroke-width="1.5"/></svg>
    <span>05:08:56</span>
  </div>
</section>

<footer>
  <div class="abs footer"></div>
  <nav class="abs foot-links">
    <a href="#">Home</a><a href="#">About Us</a><a href="#">Courses &amp; Prices</a><a href="#">Contact Us</a><a href="#">FAQ</a><a href="#">Calendar</a>
  </nav>
  <div class="abs copy">Copyright © 2013, FinTide, All Rights Reserved</div>
  <ul class="abs social" aria-label="Social links">
    <li></li><li></li><li></li><li></li>
  </ul>
</footer>

</body>
</html>
```